Brindle Office - One sheet needed for Sales Team

We need a One Sheet that introduces our business and what we do to prospective customers. This will be used both digitally and print for sales calls, both virtually and in person. Ideally we'd like this to match our branding and messaging from our website brindleofficeco.com so there is consistency with our messaging. Also, we have a desire for this to have a call to action that directs to our website and main phone where we have lead capture ability.
It should be clean and consistent with current marketing trends. We would like to include information about the business, our value proposition of being able to save customers up to 60% off their copy and printing costs, and some differentiators (i.e. 80+ point inspection of equipment, full teardown and rebuild of like new units, transparent pricing and lease options, 6 month warranty, comprehensive maintenance programs).

```html
<!DOCTYPE html>
<html lang="en">
<head>
<meta charset="utf-8">
<title>Brindle Office – One Sheet</title>
<link rel="stylesheet" href="https://fonts.googleapis.com/css2?family=Montserrat:wght@500;600;700;800&family=Open+Sans:wght@400;600&family=Oswald:wght@500;600&family=Anton&display=swap">
<style>
  :root{
    --magenta:#b5195c;
    --magenta-deep:#7e0f3f;
    --cyan:#19a4c6;
    --yellow:#f5dd00;
    --gold:#c9b400;
    --ink:#1c1c1e;
    --paper:#ffffff;
    --mist:#eeeff1;
    --teal-a:#3fb0c3;
    --teal-b:#12687e;
  }
  *{margin:0;padding:0;box-sizing:border-box}
  html,body{width:720px;height:1200px;overflow:hidden;background:var(--paper)}
  .sheet{position:relative;width:720px;height:1200px;overflow:hidden;background:linear-gradient(160deg,#fafafa,var(--mist));font-family:"Open Sans",sans-serif}
  .backdrop,.showroom{position:absolute;left:0;top:0}
  .brand{position:absolute;left:45px;top:130px;display:flex;align-items:center;gap:10px}
  .brand-dot{width:30px;height:30px;border-radius:50%;background:var(--magenta)}
  .brand-name{font-family:"Montserrat",sans-serif;font-weight:800;font-size:26px;color:var(--ink);letter-spacing:.3px}
  .photo-circle{position:absolute;border-radius:50%;border:5px solid var(--magenta);box-shadow:0 4px 14px rgba(0,0,0,.18)}
  .photo-circle.print{left:64px;top:212px;width:172px;height:172px;background:radial-gradient(circle at 55% 55%,#f2c33a,#d94c7a 35%,#4d4f55 70%,#d9d9db)}
  .photo-circle.copier{left:356px;top:425px;width:300px;height:300px;background:radial-gradient(circle at 50% 50%,#dfe3e8,#c8ced6 45%,#ffffff 72%)}
  .dot{position:absolute;border-radius:50%;background:radial-gradient(circle at 35% 30%,var(--teal-a),var(--teal-b))}
  .dot.one{left:35px;top:208px;width:70px;height:70px}
  .dot.two{left:207px;top:317px;width:44px;height:44px}
  .dot.three{left:317px;top:593px;width:110px;height:110px}
  .headline{position:absolute;left:46px;top:410px;font-family:"Montserrat",sans-serif;font-weight:800;line-height:1}
  .headline .lead{display:block;font-size:50px;color:var(--cyan)}
  .headline .sub{display:block;font-size:28px;color:var(--magenta);margin-top:6px}
  .tagline{position:absolute;left:46px;top:540px;width:300px;font-size:16px;line-height:23px;color:#333}
  .about{position:absolute;left:45px;top:696px;width:292px;color:#fff}
  .about h2{font-family:"Montserrat",sans-serif;font-weight:700;font-size:34px;line-height:1.1}
  .about .rule{display:block;width:185px;height:3px;margin:8px 0 16px;background:linear-gradient(90deg,var(--yellow) 45%,rgba(245,221,0,.5) 45%)}
  .about p{font-size:10.6px;line-height:15.2px;text-align:justify;margin-bottom:4px}
  .divider{position:absolute;left:358px;top:740px;width:1px;height:310px;background:var(--yellow)}
  .offer{position:absolute;left:378px;top:752px;width:330px;color:#fff}
  .offer .kicker{font-family:"Oswald",sans-serif;font-weight:600;font-size:40px;line-height:1}
  .offer .big{font-family:"Anton",sans-serif;font-size:96px;line-height:1;margin-top:2px;background:linear-gradient(180deg,#fff35a,var(--yellow) 45%,var(--gold));-webkit-background-clip:text;background-clip:text;color:transparent}
  .offer .costs{font-family:"Oswald",sans-serif;font-weight:600;font-size:22.5px;color:var(--yellow);line-height:1.1;margin-top:4px}
  .offer .diff{font-size:12px;line-height:16.5px;margin-top:10px;text-align:justify}
  .warranty{position:absolute;right:40px;top:1048px;text-align:right;font-family:"Montserrat",sans-serif;line-height:1}
  .warranty .months{display:block;font-weight:700;font-size:38px;color:var(--magenta)}
  .warranty .word{display:block;font-weight:700;font-size:38px;color:var(--cyan);margin-top:2px}
  .warranty .plan{display:block;font-weight:600;font-size:19px;color:var(--ink);margin-top:6px;line-height:1.2}
  .cta{position:absolute;left:42px;top:1062px}
  .cta-pill{display:inline-block;background:var(--cyan);color:#fff;font-family:"Montserrat",sans-serif;font-weight:700;font-size:26px;padding:3px 14px 4px;border-radius:0 16px 0 16px}
  .contact{list-style:none;margin-top:10px}
  .contact li{display:flex;align-items:center;gap:16px;color:#fff;font-family:"Montserrat",sans-serif;font-weight:500;font-size:19px;height:38px}
  .contact svg{width:18px;height:18px}
</style>
</head>
<body>
<main class="sheet">

  <svg class="showroom" width="720" height="1200" viewBox="0 0 720 1200" role="img" aria-label="Photo of multifunction office copiers lined up in a showroom">
    <defs>
      <linearGradient id="roomTone" x1="0" y1="0" x2="0" y2="1">
        <stop offset="0" stop-color="#a9acc4"/>
        <stop offset=".25" stop-color="#dcd9d2"/>
        <stop offset=".7" stop-color="#c9c3b8"/>
        <stop offset="1" stop-color="#6f6250"/>
      </linearGradient>
    </defs>
    <path d="M330 0 H720 V720 C600 690 470 610 420 470 C385 360 360 180 330 0 Z" fill="url(#roomTone)"/>
  </svg>

  <svg class="backdrop" width="720" height="1200" viewBox="0 0 720 1200" aria-hidden="true">
    <defs>
      <linearGradient id="wine" x1="0" y1="0" x2="0" y2="1">
        <stop offset="0" stop-color="var(--magenta)"/>
        <stop offset="1" stop-color="var(--magenta-deep)"/>
      </linearGradient>
    </defs>
    <path d="M300 0 C335 170 355 360 400 480 C440 585 520 650 620 690 L600 700 C500 660 420 590 385 485 C340 360 318 180 285 0 Z" fill="var(--magenta)"/>
    <path d="M318 60 C345 210 360 360 395 455 L388 470 C352 370 332 220 306 80 Z" fill="var(--cyan)"/>
    <path d="M420 530 C470 610 540 660 640 700 L600 710 C520 680 460 630 420 560 Z" fill="var(--ink)"/>
    <path d="M0 610 Q300 720 720 600 V1200 H0 Z" fill="url(#wine)"/>
    <rect x="0" y="1082" width="720" height="118" fill="var(--ink)"/>
    <path d="M298 1200 C340 1110 385 1055 432 1030 L436 1037 C395 1065 360 1120 334 1200 Z" fill="var(--yellow)"/>
    <path d="M316 1200 C355 1115 395 1060 434 1034 L436 1038 C398 1065 362 1122 334 1200 Z" fill="var(--cyan)"/>
    <path d="M334 1200 C370 1120 400 1062 436 1038 C520 1008 640 995 720 985 V1200 Z" fill="var(--paper)"/>
  </svg>

  <div class="brand">
    <span class="brand-dot"></span>
    <span class="brand-name">Brindle Office</span>
  </div>

  <div class="photo-circle print" role="img" aria-label="Close-up photo of a printer output tray with colourful prints"></div>
  <div class="dot one"></div>
  <div class="dot two"></div>

  <h1 class="headline">
    <span class="lead">HELPING</span>
    <span class="sub">BUSINESS OWNERS<br>SAVE MONEY</span>
  </h1>
  <p class="tagline">Smart Office &amp; Work From Home Print Solutions By Norvale, Kestrel, Aldren Imaging, Tavix &amp; Quillon</p>

  <div class="photo-circle copier" role="img" aria-label="Product photo of a large multifunction office copier"></div>
  <div class="dot three"></div>

  <section class="about">
    <h2>About us</h2>
    <span class="rule"></span>
    <p>Brindle Office was formed in 1986, and has been serving the Tri-County community for over three decades as a premier copier sales, service, and rental co. We offer the finest in state of the art equipment from manufacturers such as Norvale, Kestrel, and Aldren Imaging.</p>
    <p>Brindle Office offers the finest in state of the art equipment from manufacturers such as Norvale, Kestrel, and Aldren Imaging. In addition to new equipment, we also rent, lease, and sell refurbished copiers. These copiers are fully reconditioned and warranted to give many years of high quality performance to the cost conscious business.</p>
    <p>Since we carry over a million dollars in supplies and parts, Brindle Office is able to provide maintenance agreements on most copiers. We offer a two hour response time on all repairs within the Tri-County area. Our technicians have a minimum of 10 years repair experience and a combined total of 79 years!</p>
  </section>

  <div class="divider"></div>

  <section class="offer">
    <p class="kicker">SAVE UP TO</p>
    <p class="big">60% off</p>
    <p class="costs">THEIR COPY AND PRINTING COSTS,</p>
    <p class="diff">and some differentiators (i.e. 80+ point inspection of equipment, full teardown and rebuild of like new units, transparent pricing and lease options</p>
  </section>

  <section class="warranty">
    <span class="months">6 MONTH</span>
    <span class="word">WARRANTY</span>
    <span class="plan">COMPREHENSIVE<br>MAINTENANCE PROGRAMS</span>
  </section>

  <section class="cta">
    <span class="cta-pill">Contact us now!</span>
    <ul class="contact">
      <li>
        <svg viewBox="0 0 24 24" aria-hidden="true"><path d="M6.6 10.8a15 15 0 0 0 6.6 6.6l2.2-2.2a1 1 0 0 1 1-.25 11.4 11.4 0 0 0 3.6.6 1 1 0 0 1 1 1V20a1 1 0 0 1-1 1A17 17 0 0 1 3 4a1 1 0 0 1 1-1h3.5a1 1 0 0 1 1 1 11.4 11.4 0 0 0 .6 3.6 1 1 0 0 1-.25 1z" fill="#e2437f"/></svg>
        <span>+1 555-013-2808</span>
      </li>
      <li>
        <svg viewBox="0 0 24 24" aria-hidden="true"><g fill="none" stroke="#e2437f" stroke-width="2"><circle cx="12" cy="12" r="9"/><ellipse cx="12" cy="12" rx="4" ry="9"/><path d="M3 12h18M5 7h14M5 17h14"/></g></svg>
        <span>www.brindleofficeco.com</span>
      </li>
    </ul>
  </section>

</main>
</body>
</html>
```